Media One Sheet given to producers to promote myself as guest on their show

I need a media one sheet which I will give to radio and television producers. It will help them understand why I would be a great guest for their show(s) and who I am. I've provided a template as well as a rough draft. I need the rough draft adapted to the new template provided. There are also edit notes to help guide the development.

Target Market(s)

tv and radio producers

Industry/Entity Type

Media

Colors
cadf82
87cfc6

Requirements
Must have
• elements laid out in template
Nice to have
• professional very polished feel
Should not have
• references to my start up company (as stated in the edits document). Story ideas, photo of handbags, photo of myself, contact info
• Please follow template as guide.

```html
<!DOCTYPE html>
<html lang="en">
<head>
<meta charset="utf-8">
<title>Dana Whitfield – Media One Sheet</title>
<link rel="stylesheet" href="https://fonts.googleapis.com/css2?family=Montserrat:ital,wght@0,400;0,500;0,600;0,700;1,500&family=Great+Vibes&display=swap">
<style>
:root{
  --lime:#cadf82;
  --slate:#8a9e9c;
  --teal:#87cfc6;
  --teal-soft:#c3e6e4;
  --teal-ring:#5fc0ae;
  --deep:#1d6b5b;
  --band:#22705f;
  --accent:#2aa58f;
  --ink:#111;
  --white:#fff;
}
*{margin:0;padding:0;box-sizing:border-box}
html,body{width:927px;height:1200px;overflow:hidden;background:var(--white)}
body{font-family:'Montserrat',sans-serif;color:var(--ink)}
.sheet{position:relative;width:927px;height:1200px;overflow:hidden;background:var(--white)}
.abs{position:absolute}
.band-lime{left:0;top:0;width:927px;height:26px;background:var(--lime)}
.band-slate{left:0;top:29px;width:927px;height:14px;background:var(--slate)}
.header{left:0;top:46px;width:927px;height:271px;background:var(--teal)}
.kicker{left:50px;top:56px;color:var(--white);font-size:28.5px;font-weight:500;line-height:38px}
.pitch{left:448px;top:138px;color:var(--deep)}
.pitch .lead{font-size:27px;font-weight:400;line-height:34px}
.pitch .big{font-size:50px;font-weight:700;line-height:58px;margin-top:-2px}
.pitch .sub{font-size:24px;font-weight:400;line-height:30px;margin-top:4px}
.pitch .strong{font-size:34.5px;font-weight:700;line-height:38px}
.portrait-ring{left:48px;top:144px;width:352px;height:352px;border-radius:50%;background:linear-gradient(160deg,#9bd9cf,#cdeeea);border:6px solid var(--teal-ring)}
.portrait{left:68px;top:164px;width:312px;height:312px;border-radius:50%;background:radial-gradient(circle at 50% 45%,#e6cfa8,#c7b07a 55%,#8f8b55)}
.name{left:0;top:506px;width:448px;text-align:center;font-size:29px;font-weight:600}
.role{left:0;top:545px;width:448px;text-align:center;font-size:20px}
.tagline{left:0;top:584px;width:448px;text-align:center;font-family:'Great Vibes',cursive;color:var(--accent);font-size:33px;line-height:40px}
.product-photo{left:450px;top:325px;width:477px;height:310px;background:linear-gradient(135deg,#7c8a5a,#c59c62 45%,#a7a59a 75%,#6f7055)}
.brand-badge{left:712px;top:528px;width:176px;height:176px;border-radius:50%;background:var(--white);display:flex;flex-direction:column;align-items:center;justify-content:center;gap:8px}
.brand-badge .dot{width:60px;height:60px;border-radius:50%;background:var(--accent)}
.brand-badge .brand{font-size:15px;font-weight:600;color:var(--deep)}
.contact-band{left:0;top:1053px;width:927px;height:127px;background:var(--band)}
.stories{left:0;top:693px;width:430px;height:461px;background:var(--teal-soft);border-radius:0 18px 18px 0;overflow:hidden;box-shadow:2px 2px 6px rgba(0,0,0,.15)}
.stories .head{height:54px;background:var(--teal);padding:14px 0 0 30px;font-size:22px;font-weight:500;color:var(--deep)}
.dots{display:inline-block;width:238px;border-bottom:1.5px dotted var(--deep);margin-left:2px}
.stories ul{list-style:none;padding:6px 30px 0 30px}
.stories li{font-size:15.5px;line-height:20px;margin-bottom:16px;text-align:justify}
.stories li::before{content:"•";margin-left:-6px;margin-right:4px}
.stories li .angle{display:block;margin-top:8px;padding-left:15px;color:var(--accent);font-style:italic;font-weight:500}
.media{left:464px;top:723px;width:428px}
.media h2{font-size:22.5px;font-weight:600;color:var(--deep)}
.media h2 .dots{width:208px}
.media p{font-size:15.5px;line-height:20px;text-align:justify;margin-top:16px}
.media h2 + p{margin-top:12px}
.contact{left:474px;top:1060px;color:var(--white)}
.contact .who{font-size:20.5px;font-weight:600;margin-bottom:6px}
.contact .row{display:flex;align-items:center;gap:10px;font-size:17px;line-height:26px}
.contact svg{width:15px;height:15px;fill:var(--white)}
</style>
</head>
<body>
<main class="sheet">
  <div class="abs band-lime"></div>
  <div class="abs band-slate"></div>
  <div class="abs header"></div>

  <h1 class="abs kicker">From the Purse You Carry … to the Cookies<br>You Buy in the Supermarket</h1>

  <div class="abs pitch">
    <p class="lead">This Social Entrepreneur</p>
    <p class="big">Reveals</p>
    <p class="sub">How Consumers and Business Can</p>
    <p class="strong">Do Better by Doing Good</p>
  </div>

  <div class="abs portrait-ring"></div>
  <div class="abs portrait" role="img" aria-label="Portrait photo of Dana Whitfield outdoors"></div>

  <p class="abs name">Dana Whitfield</p>
  <p class="abs role">Social Entrepreneur and Radio Host</p>
  <p class="abs tagline">Making a Positive<br>Social Impact Is Better Business</p>

  <div class="abs product-photo" role="img" aria-label="Photo of three wicker handbags with coloured leather straps on a log"></div>
  <div class="abs brand-badge">
    <span class="dot"></span>
    <span class="brand">Tote &amp; Thread</span>
  </div>

  <div class="abs contact-band"></div>

  <section class="abs stories">
    <h2 class="head">Story Ideas<span class="dots"></span></h2>
    <ul>
      <li>How to make empowered choices when shopping for fashion and accessories.<span class="angle">What natural materials and seals of approval to look for</span></li>
      <li>How the foods you purchase at the supermarket may be killing the Rain Forest.<span class="angle">All about palm oil, it’s impact on our environment and use in the snack industry.</span></li>
      <li>Why it’s time to bring back made in the USA.<span class="angle">How our re-shoring efforts can improve the economy and the environment.</span></li>
      <li>What is a Social Entrepreneur and can it be more profitable?<span class="angle">Studies have revealed socially conscious businesses tend to be more profitable over the long-term</span></li>
    </ul>
  </section>

  <section class="abs media">
    <h2>Media Experience<span class="dots"></span></h2>
    <p>Whitfield has hosted the Common Ground Radio podcast on KRVL 98.3, Ridgeline Community Radio, for __ years. The show discusses social enterprise, conscious business practices and the impacts business can have on social, cultural and environmental health.</p>
    <p>A FundSpark Crowdfunding campaign that raised $9,180 for her Tote &amp; Thread product launch, netted her publicity on 30 websites.</p>
    <p>In addition, she has given talks on practice management, orthodontics and ClearAlign, as far away as China.</p>
  </section>

  <address class="abs contact" style="font-style:normal">
    <p class="who">Dana Whitfield</p>
    <p class="row"><svg viewBox="0 0 24 24"><path d="M12 2a7 7 0 0 0-7 7c0 5 7 13 7 13s7-8 7-13a7 7 0 0 0-7-7zm0 9.5A2.5 2.5 0 1 1 12 6.5a2.5 2.5 0 0 1 0 5z"/></svg>P.O. Box 1450, Helena, Mt.&nbsp; 59601</p>
    <p class="row"><svg viewBox="0 0 24 24"><rect x="1" y="1" width="22" height="22" rx="4"/><path fill="#22705f" d="M8 5l2 4-1.5 1.5a9 9 0 0 0 5 5L15 14l4 2v2a2 2 0 0 1-2 2A12 12 0 0 1 4 7a2 2 0 0 1 2-2z"/></svg>555-014-2380</p>
    <p class="row"><svg viewBox="0 0 24 24"><path d="M2 5h20v2l-10 6L2 7z"/><path d="M2 9l10 6 10-6v10H2z"/></svg>dwhitfield@toteandthread.net</p>
  </address>
</main>
</body>
</html>
```